Coaching business needs flyer for business market

I need a flyer that I can send to HR-managers and business owners to inform them of my coaching services for organisations. We have three services: organisational- and teamcoaching, individual coaching and training programs.
I want the flyer to express calmness, solid and trustworthy coaching. As a person I am open and think out of the box.

In my logo I use a couple of colours (blue, green, orange and grey) that represent the diversity of humans. My company's name is Bramblecrest Engagement & Coaching and tag line is "Awaken your quiet river".

I do not want the design to be too busy but also not too boring. I tried making something myself. Feel free to build on that design. Or feel free to start from scratch.

```html
<!DOCTYPE html>
<html lang="nl">
<head>
<meta charset="utf-8">
<title>Bramblecrest Engagement &amp; Coaching – flyer</title>
<link rel="stylesheet" href="https://fonts.googleapis.com/css2?family=Ubuntu:wght@400;500;700&display=swap">
<style>
  :root {
    --page-bg: #e9e7e4;
    --frame-orange: #f29a1f;
    --paper: #ffffff;
    --title-red: #ec6459;
    --heading-red: #e4463b;
    --teal: #1b9aa2;
    --orange: #f0961c;
    --navy: #27508f;
    --text: #2a2a2a;
    --logo-grey: #6b6f74;
    --portrait-blue: #2f5fd2;
  }
  * { margin: 0; padding: 0; box-sizing: border-box; }
  html, body { width: 1200px; height: 800px; overflow: hidden; }
  body {
    background: var(--page-bg);
    font-family: "Ubuntu", sans-serif;
    color: var(--text);
    position: relative;
  }
  .flyer {
    position: absolute;
    left: 330px; top: 15px;
    width: 540px; height: 770px;
    background: var(--frame-orange);
    border-radius: 6px;
    box-shadow: 0 6px 18px rgba(0,0,0,.18);
  }
  .sheet {
    position: absolute;
    inset: 12px;
    background: var(--paper);
    border-radius: 18px;
  }
  .block { position: absolute; }

  .brand {
    right: 18px; top: 18px; width: 200px;
    display: flex; align-items: center; justify-content: flex-end; gap: 9px;
  }
  .brand-dot {
    flex: none; width: 28px; height: 28px; border-radius: 50%;
    background: var(--teal);
  }
  .brand-name {
    font-size: 13px; font-weight: 400; line-height: 1.2;
    color: var(--logo-grey);
    white-space: nowrap;
  }

  .title-box {
    left: 18px; top: 70px; width: 262px; height: 84px;
    background: var(--title-red);
    border-radius: 14px;
    display: flex; align-items: center;
    padding: 0 20px;
  }
  .title-box h1 {
    color: #fff; font-weight: 700; font-size: 29px; line-height: 1.05;
    text-transform: uppercase; letter-spacing: .5px;
  }

  .photo {
    border-radius: 14px;
    border: 2px solid;
  }
  .photo-portrait {
    left: 318px; top: 68px; width: 180px; height: 126px;
    background: radial-gradient(circle at 55% 55%, #5a7fe0 0%, var(--portrait-blue) 55%, #2448b5 100%);
    border-color: #3a62b5;
  }
  .photo-team {
    left: 18px; top: 286px; width: 152px; height: 114px;
    background: linear-gradient(135deg, #c9a07a, #e5d3c0 55%, #8c7a6c);
    border-color: var(--heading-red);
  }
  .photo-duo {
    left: 370px; top: 388px; width: 136px; height: 96px;
    background: linear-gradient(135deg, #d8c3a2, #efe4d0 50%, #6f86a8);
    border-color: var(--teal);
  }
  .photo-event {
    left: 18px; top: 506px; width: 152px; height: 112px;
    background: linear-gradient(160deg, #4b3f7a, #1f1b33 60%, #2d3a5a);
    border-color: var(--orange);
  }
  .photo-room {
    left: 382px; top: 540px; width: 124px; height: 88px;
    background: linear-gradient(150deg, #cfd6da, #e8e6e0 50%, #b98a55);
    border-color: var(--heading-red);
  }

  .intro {
    left: 18px; top: 162px; width: 292px;
    font-size: 8.4px; line-height: 1.38;
  }
  .intro .person { color: var(--navy); font-weight: 700; text-transform: uppercase; }

  .service h2 {
    font-size: 10.4px; font-weight: 700; line-height: 1.25;
    margin-bottom: 4px;
  }
  .service-red h2 { color: var(--heading-red); }
  .service-teal h2 { color: var(--teal); }
  .service-orange h2 { color: var(--orange); }

  .checklist { list-style: none; }
  .checklist li {
    display: flex; align-items: flex-start; gap: 6px;
    font-size: 8.6px; line-height: 1.3; margin-bottom: 2.5px;
  }
  .checklist svg { flex: none; width: 10px; height: 10px; margin-top: 1px; }
  .service-red .checklist svg { color: var(--heading-red); }
  .service-teal .checklist svg { color: var(--teal); }
  .service-orange .checklist svg { color: var(--orange); }

  .service-organisation { left: 184px; top: 286px; width: 318px; }
  .service-individual { left: 18px; top: 408px; width: 345px; }
  .service-training { left: 184px; top: 504px; width: 322px; }
  .service-training .checklist { width: 190px; }
  .service-methods { left: 18px; top: 634px; width: 488px; }
</style>
</head>
<body>
<svg width="0" height="0" style="position:absolute" aria-hidden="true">
  <symbol id="tick-box" viewBox="0 0 12 12">
    <rect x="0.8" y="1.8" width="9.4" height="9.4" rx="1.5" fill="none" stroke="currentColor" stroke-width="1.3"/>
    <path d="M2.8 6.2 L5.2 8.6 L11.2 1.4" fill="none" stroke="currentColor" stroke-width="1.7" stroke-linecap="round" stroke-linejoin="round"/>
  </symbol>
</svg>

<main class="flyer">
  <div class="sheet">
    <div class="block brand">
      <span class="brand-dot"></span>
      <span class="brand-name">Bramblecrest<br>Engagement &amp; Coaching</span>
    </div>

    <div class="block title-box"><h1>Awaken your<br>quiet river</h1></div>

    <div class="block photo photo-portrait" role="img" aria-label="Portretfoto van de coach tegen een blauwe achtergrond"></div>

    <p class="block intro"><span class="person">Marisol Venhuizen</span> is trainer en coach. Ze heeft ruime ervaring met veranderingstrajecten binnen organisaties. Mensen omschrijven haar als ‘betrokken, warm, stevig en kordaat’. Het is haar passie om organisaties, teams en mensen te helpen groeien. Zij helpt weerstand te overwinnen en draagt bij aan groei in zelfvertrouwen. Haar trainingen en coaching zijn erop gericht om snel inzichtelijk te krijgen welke stappen men moet zetten om verder te komen. Ze gelooft de veranderkracht van de mensen waar ze mee werkt. Ze is er om steun en richting te bieden en laat hen zelf aan het roer.</p>

    <div class="block photo photo-team" role="img" aria-label="Foto van een teamsessie in een lichte ruimte"></div>

    <section class="block service service-red service-organisation">
      <h2>Een organisatie waar medewerkers gemotiveerd zijn, samenwerken, communiceren zonder gedoe door ORGANISATIE- of TEAM coaching:</h2>
      <ul class="checklist">
        <li><svg><use href="#tick-box"/></svg>Heb je zorgen voor of na een fusie of verandering?</li>
        <li><svg><use href="#tick-box"/></svg>Wil je missie, visie &amp; strategie ontwikkelen of wijzigen?</li>
        <li><svg><use href="#tick-box"/></svg>Wens je de cultuur-veranderen of verder ontwikkelen?</li>
        <li><svg><use href="#tick-box"/></svg>Beoog je de samenwerking bevorderen of verbeteren?</li>
      </ul>
    </section>

    <div class="block photo photo-duo" role="img" aria-label="Foto van een individueel coachgesprek"></div>

    <section class="block service service-teal service-individual">
      <h2>Duurzame Inzetbaarheid door INDIVIDUELE Coaching:</h2>
      <ul class="checklist">
        <li><svg><use href="#tick-box"/></svg>Wens je medewerkers die hun talent ten volste benutten?</li>
        <li><svg><use href="#tick-box"/></svg>Verlang je meer authentieke leiderschap bij je collega’s?</li>
        <li><svg><use href="#tick-box"/></svg>Wil je de mensen vooruit helpen in hun loopbaan?</li>
        <li><svg><use href="#tick-box"/></svg>Zoek je steun voor medewerkers met burn-out of re-integratie?</li>
        <li><svg><use href="#tick-box"/></svg>Heb je hulp nodig bij outplacement trajecten?</li>
      </ul>
    </section>

    <div class="block photo photo-event" role="img" aria-label="Foto van een workshop voor publiek in een zaal"></div>

    <section class="block service service-orange service-training">
      <h2>Ontwikkeling and Borging van kennis en vakmanschap door LEERGANGEN, TRAININGEN &amp; WORKSHOPS op MAAT</h2>
      <ul class="checklist">
        <li><svg><use href="#tick-box"/></svg>Leiderschap</li>
        <li><svg><use href="#tick-box"/></svg>Communicatie</li>
        <li><svg><use href="#tick-box"/></svg>Leren kijken met ‘systemische blik’ voor professionals</li>
        <li><svg><use href="#tick-box"/></svg>Conflicthantering</li>
      </ul>
    </section>

    <div class="block photo photo-room" role="img" aria-label="Foto van een training in een kring"></div>

    <section class="block service service-red service-methods">
      <h2>Gedegen resultaat en kwaliteit door bewezen ‘best practices’</h2>
      <ul class="checklist">
        <li><svg><use href="#tick-box"/></svg>Neuro Linguïstisch Programmeren (NLP)</li>
        <li><svg><use href="#tick-box"/></svg>Transactionele Analyse</li>
        <li><svg><use href="#tick-box"/></svg>Systemisch Werken: Organisatieopstellingen, Familieopstellingen, Identity oriented Psycho Traumaopstellingen)</li>
        <li><svg><use href="#tick-box"/></svg>Somatic Experience, Ademwerk en Lichaamswerk</li>
      </ul>
    </section>
  </div>
</main>
</body>
</html>
```